KerrLow Farm

Need a nice simple clean double sided business card that has our logo and info on:
Kerr Low Farm
Martin & Felicity Kerr Low
kerrlowfarm@mailbarn.example
Martin: 1-780-555-0148
Felicity: 1-780-555-0193
Instagram @ kerrlow_farm

Contact Information for Business Card

Martin & Felicity Kerr Low kerrlowfarm@mailbarn.example Martin: 1-780-555-0148 Felicity: 1-780-555-0193

```html
<!DOCTYPE html>
<html lang="en">
<head>
<meta charset="utf-8">
<title>Kerr Low Farm – Business Card</title>
<link rel="stylesheet" href="https://fonts.googleapis.com/css2?family=Arvo:wght@400;700&display=swap">
<style>
  :root {
    --farm-green: #3f7a27;
    --harvest-orange: #f39c12;
    --card-white: #f7f7f5;
    --desk-grey: #d9dadd;
    --ink-white: #ffffff;
  }
  html, body {
    margin: 0;
    padding: 0;
    width: 1200px;
    height: 800px;
    overflow: hidden;
    background: var(--desk-grey);
  }
  .canvas {
    width: 1200px;
    height: 800px;
    display: flex;
    align-items: center;
    justify-content: center;
    gap: 48px;
  }
  .business-card {
    width: 520px;
    height: 297px;
    box-shadow: 0 6px 18px rgba(0,0,0,0.18);
    background: var(--card-white);
  }
  .business-card svg { display: block; }
  .card-text { font-family: 'Arvo', serif; }
  .fill-green { fill: var(--farm-green); }
  .fill-orange { fill: var(--harvest-orange); }
  .fill-white { fill: var(--card-white); }
  .front-email { fill: var(--ink-white); font-size: 15px; }
  .owner-first { fill: var(--farm-green); font-size: 23px; }
  .owner-last { fill: var(--harvest-orange); font-size: 23px; }
  .brand-name { fill: var(--farm-green); font-size: 19px; letter-spacing: 1px; }
  .brand-ring { fill: none; stroke: var(--farm-green); stroke-width: 3; }
  .contact-line { fill: var(--ink-white); font-size: 12.5px; }
  .contact-icon { fill: var(--ink-white); }
  .contact-icon-outline { fill: none; stroke: var(--ink-white); stroke-width: 1.6; }
  .envelope-fold { fill: none; stroke: var(--farm-green); stroke-width: 1.2; }
</style>
</head>
<body>
<main class="canvas">

  <section class="business-card card-front" aria-label="Card front">
    <svg width="520" height="297" viewBox="0 0 520 297">
      <rect class="fill-white" width="520" height="297"/>
      <path class="fill-orange" d="M0 0 H520 V126 C430 110 330 124 250 180 C170 236 80 252 0 248 Z"/>
      <path class="fill-green" d="M0 0 H520 V110 C430 95 330 110 240 170 C160 225 80 250 0 248 Z"/>
      <text class="card-text front-email" x="40" y="86">kerrlowfarm@mailbarn.example</text>
    </svg>
  </section>

  <section class="business-card card-back" aria-label="Card back">
    <svg width="520" height="297" viewBox="0 0 520 297">
      <rect class="fill-white" width="520" height="297"/>
      <path class="fill-orange" d="M0 170 C120 145 250 148 340 172 C420 192 470 188 520 158 V297 H0 Z"/>
      <path class="fill-green" d="M0 186 C120 160 240 163 330 184 C420 205 470 198 520 172 V297 H0 Z"/>

      <g class="owner-names card-text">
        <text class="owner-first" x="28" y="98">Martin &amp; Felicity</text>
        <text class="owner-last" x="28" y="126">Kerr Low</text>
      </g>

      <g class="brand-mark">
        <circle class="brand-ring" cx="405" cy="62" r="36"/>
        <text class="card-text brand-name" x="405" y="128" text-anchor="middle">KERR LOW FARM</text>
      </g>

      <g class="contact-list card-text">
        <g class="contact-item">
          <rect class="contact-icon" x="40" y="214" width="13" height="9" rx="1"/>
          <path class="envelope-fold" d="M40 215 L46.5 220 L53 215"/>
          <text class="contact-line" x="62" y="223">kerrlowfarm@mailbarn.example</text>
        </g>
        <g class="contact-item">
          <path class="contact-icon" d="M42 232 q2 -2 4 0 l1 3 q-1 1 -2 2 q1 3 4 4 q1 -1 2 -2 l3 1 q2 2 0 4 q-2 2 -5 0 q-5 -3 -7 -7 q-2 -3 0 -5 Z"/>
          <text class="contact-line" x="62" y="243">Martin: 1-780-555-0148</text>
        </g>
        <g class="contact-item">
          <path class="contact-icon" d="M42 252 q2 -2 4 0 l1 3 q-1 1 -2 2 q1 3 4 4 q1 -1 2 -2 l3 1 q2 2 0 4 q-2 2 -5 0 q-5 -3 -7 -7 q-2 -3 0 -5 Z"/>
          <text class="contact-line" x="62" y="263">Felicity: 1-780-555-0193</text>
        </g>
        <g class="contact-item">
          <rect class="contact-icon-outline" x="41" y="272" width="11" height="11" rx="2"/>
          <text class="contact-line" x="62" y="282">@ kerrlow_farm</text>
        </g>
      </g>
    </svg>
  </section>

</main>
</body>
</html>
```